QuillaVorn needs a dashboard page designed

Redesign the dashboard shown in the provided images.

There are two images:
- dashboard.png
- dashboard-expanded.png

NOTE: The vocabulary navigation on the left will be a very long list of words 100s, so keep that in mind when you're designing both the vocab navigation and the expanded vocab popup.

In the dashboard.png picture, there needs to be a progress chart showing the word progress like the following: review 1(show it as completed) -> review 2(show the user they are here) -> review 3(unvisited) -> review 4(unvisited)

The do-not-design-this-page.png image is for your reference only. It is not to be designed. Use it to understand the overall look and feel of the website to help you create the best dashboard page possible.
Updates

Need extra days to review

Industry/Entity Type

Education English learning

Number of Pages Required

1 page

Requirements
Must have
• The main navigation and main header cannot change between pages. See the do-not-design page for the main navigateion and header.
Should not have
• Do not add a person profile. We will not have images of our users. Keep the icons in the main navigation as they are.

```html
<!DOCTYPE html>
<html lang="en">
<head>
<meta charset="utf-8">
<title>QuillaVorn Tutor – Vocabulary Dashboard</title>
<link href="https://fonts.googleapis.com/css2?family=Roboto:wght@400;500;700&display=swap" rel="stylesheet">
<style>
:root{
  --topbar:#2b3340;
  --rail:#323a47;
  --rail-active:#414a58;
  --ink:#1f2328;
  --text:#3d4148;
  --muted:#8a8f96;
  --line:#e3e5e8;
  --accent:#d71920;
  --green:#22a35a;
  --panel:#f4f4f5;
  --bar:#2a5eab;
  --tip:#3a3f46;
}
*{box-sizing:border-box;margin:0;padding:0}
html,body{width:1200px;height:675px;overflow:hidden}
body{font-family:"Roboto",Arial,sans-serif;color:var(--text);background:#fff;position:relative;font-size:10.5px}
.topbar{position:absolute;left:0;top:0;width:1200px;height:25px;background:var(--topbar);color:#fff}
.topbar .brand{position:absolute;left:0;right:0;top:6px;text-align:center;font-size:10.5px;font-weight:500}
.topbar .tools{position:absolute;right:8px;top:5px;display:flex;gap:14px;align-items:center}
.rail{position:absolute;left:0;top:25px;width:52px;height:650px;background:var(--rail)}
.rail .item{height:54px;display:flex;flex-direction:column;align-items:center;justify-content:center;gap:3px;color:#fff;font-size:6px;text-align:center}
.rail .item.active{background:var(--rail-active)}
.sidebar{position:absolute;left:52px;top:25px;width:240px;height:650px;border-right:1px solid var(--line)}
.select{position:absolute;left:18px;top:18px;width:168px;height:30px;border:1px solid #c9ccd0;border-radius:3px;padding:0 9px;display:flex;align-items:center;justify-content:space-between;font-size:10.5px;color:var(--ink)}
.expand{position:absolute;left:192px;top:18px;width:30px;height:30px;border:1px solid #c9ccd0;border-radius:3px;display:flex;align-items:center;justify-content:center}
.group{position:absolute;left:18px;width:204px}
.group-head{height:28px;display:flex;align-items:center;gap:9px;font-weight:500;color:var(--ink);font-size:10.5px}
.group-head .info{margin-left:auto}
.words{list-style:none;margin-left:21px}
.words li{height:27.7px;display:flex;align-items:center;border-bottom:1px solid var(--line);font-size:10.5px}
.words li.current{border-left:2px solid var(--accent);padding-left:10px;color:var(--ink);font-weight:500;border-top:1px solid var(--line);background:#fff}
.scroll{position:absolute;left:216px;top:160px;width:3px;height:178px;background:#e6e7e9;border-radius:2px}
.tooltip{position:absolute;left:280px;top:139px;width:151px;height:60px;background:var(--tip);color:#fff;font-size:8.3px;line-height:12px;padding:6px 9px;border-radius:3px;z-index:2}
.tooltip::before{content:"";position:absolute;left:-5px;top:26px;border:5px solid transparent;border-left:0;border-right-color:var(--tip)}
.header{position:absolute;left:292px;top:25px;width:908px;height:68px;border-bottom:1px solid var(--line)}
.header h1{position:absolute;left:30px;top:16px;font-size:27px;font-weight:700;color:var(--ink);display:flex;align-items:center;gap:12px}
.steps{position:absolute;left:392px;top:26px;display:flex;align-items:center;font-size:10.5px;font-weight:500}
.step{display:flex;align-items:center;gap:6px}
.step.done{color:var(--green)}
.step.now{color:var(--ink)}
.step.todo{color:#b0b4b9}
.dots{width:20px;border-top:1.5px dotted #b9bcc1;margin:0 8px}
.start{position:absolute;left:776px;top:19px;width:102px;height:30px;background:var(--accent);color:#fff;border-radius:3px;display:flex;align-items:center;justify-content:center;gap:8px;font-weight:500;font-size:10.5px}
.main{position:absolute;left:292px;top:93px;width:638px;height:582px}
.section-title{position:absolute;left:30px;display:flex;align-items:center;gap:14px;font-size:13.5px;font-weight:500;color:var(--ink)}
.para{position:absolute;left:30px;width:580px;line-height:15px;font-size:10.5px}
.para b{color:var(--ink)}
.chart{position:absolute;left:30px;top:240px;width:578px;height:222px;border:1px solid var(--line);border-radius:4px}
.analysis{position:absolute;left:930px;top:93px;width:270px;height:582px;background:var(--panel);padding:0 30px}
.analysis h2{display:flex;gap:15px;align-items:center;font-size:13.5px;font-weight:500;color:var(--ink);line-height:16px;padding:30px 0 12px;border-bottom:1px solid var(--line)}
.analysis p{font-size:10.5px;line-height:15px;padding:12px 0 13px;border-bottom:1px solid var(--line)}
.analysis p:last-child{border-bottom:0}
</style>
</head>
<body>
<header class="topbar">
  <div class="brand">QuillaVorn Tutor ▾</div>
  <div class="tools">
    <svg width="12" height="12" viewBox="0 0 24 24" fill="#fff"><path d="M12 8a4 4 0 100 8 4 4 0 000-8zm9 5.5v-3l-2.6-.5a7 7 0 00-.8-1.9l1.5-2.2-2.1-2.1-2.2 1.5a7 7 0 00-1.9-.8L12.5 2h-3l-.5 2.6a7 7 0 00-1.9.8L4.9 3.9 2.8 6l1.5 2.2a7 7 0 00-.8 1.9L1 10.5v3l2.6.5c.2.7.4 1.3.8 1.9l-1.5 2.2 2.1 2.1 2.2-1.5c.6.4 1.2.6 1.9.8l.5 2.6h3l.5-2.6c.7-.2 1.3-.4 1.9-.8l2.2 1.5 2.1-2.1-1.5-2.2c.4-.6.6-1.2.8-1.9z"/></svg>
    <svg width="12" height="12" viewBox="0 0 24 24" fill="#fff"><path d="M12 1l9 4v6c0 6-4 10-9 12-5-2-9-6-9-12V5z"/><path d="M7 12l3 3 6-6" stroke="#2b3340" stroke-width="2.4" fill="none"/></svg>
    <svg width="22" height="12" viewBox="0 0 40 24"><circle cx="12" cy="12" r="11" fill="#fff"/><circle cx="12" cy="9" r="4" fill="#2b3340"/><path d="M5 19a8 8 0 0114 0" fill="#2b3340"/><path d="M30 10l4 4 4-4" stroke="#fff" stroke-width="2" fill="none"/></svg>
  </div>
</header>

<nav class="rail">
  <div class="item active"><svg width="11" height="11" viewBox="0 0 24 24" fill="#fff"><path d="M12 3l10 9h-3v9h-5v-6h-4v6H5v-9H2z"/></svg>QuillaVorn Tutor</div>
  <div class="item"><svg width="14" height="12" viewBox="0 0 24 20" fill="#fff"><path d="M1 4l7-3 8 3 7-3v15l-7 3-8-3-7 3z"/></svg>Daily English</div>
  <div class="item"><svg width="10" height="12" viewBox="0 0 20 24" fill="#fff"><path d="M2 1h16v22H2z"/><path d="M6 5h2v2H6zm6 0h2v2h-2zM6 10h2v2H6zm6 0h2v2h-2zM8 17h4v6H8z" fill="#323a47"/></svg>Business</div>
</nav>

<aside class="sidebar">
  <div class="select">All Categories <svg width="10" height="6" viewBox="0 0 10 6"><path d="M1 1l4 4 4-4" stroke="var(--accent)" stroke-width="1.4" fill="none"/></svg></div>
  <div class="expand"><svg width="12" height="12" viewBox="0 0 12 12" stroke="var(--accent)" stroke-width="1.3" fill="none"><path d="M7 1h4v4M11 1L7 5M5 11H1V7M1 11l4-4"/></svg></div>

  <div class="group" style="top:84px">
    <div class="group-head"><svg width="11" height="11" viewBox="0 0 24 24" fill="none" stroke="#1f2328" stroke-width="2.4"><circle cx="12" cy="13" r="9"/><path d="M12 8v5M9 1h6"/></svg>Short-Term Memory<svg class="info" width="11" height="11" viewBox="0 0 24 24" fill="none" stroke="#aaa" stroke-width="1.6"><circle cx="12" cy="12" r="10"/><path d="M12 10v7M12 6v1"/></svg></div>
    <ul class="words"><li class="current">Grab</li></ul>
  </div>

  <div class="group" style="top:154px">
    <div class="group-head"><svg width="12" height="12" viewBox="0 0 24 24" fill="none" stroke="#1f2328" stroke-width="2.2"><rect x="6" y="6" width="12" height="12"/><path d="M9 2v4M15 2v4M9 18v4M15 18v4M2 9h4M2 15h4M18 9h4M18 15h4"/></svg>Working Memory<svg class="info" width="11" height="11" viewBox="0 0 24 24" fill="none" stroke="var(--accent)" stroke-width="1.8"><circle cx="12" cy="12" r="10"/><path d="M12 10v7M12 6v1"/></svg></div>
    <ul class="words">
      <li>Cool Down</li><li>Crave</li><li>Go For</li><li>Go-To</li><li>In The Mood For</li><li>Grab</li><li>Sip</li><li>Soothing</li>
    </ul>
  </div>
  <div class="scroll"></div>

  <div class="group" style="top:419px">
    <div class="group-head"><svg width="11" height="11" viewBox="0 0 24 24" fill="none" stroke="#1f2328" stroke-width="2.4"><rect x="4" y="10" width="16" height="12" rx="2"/><path d="M8 10V7a4 4 0 018 0v3"/></svg>Long-Term Memory<svg class="info" width="11" height="11" viewBox="0 0 24 24" fill="none" stroke="#aaa" stroke-width="1.6"><circle cx="12" cy="12" r="10"/><path d="M12 10v7M12 6v1"/></svg></div>
    <ul class="words"><li>Give It A Try</li></ul>
  </div>
</aside>

<div class="tooltip">Tooltip information goes here lorem ipsum dolor sit amet consectetur adipiscing elit sed do eiusmod tempor incididunt.</div>

<section class="header">
  <h1>Grab <svg width="15" height="15" viewBox="0 0 24 24" fill="#f5b21b"><path d="M12 2l3 7 7.5.6-5.7 4.9 1.8 7.4L12 18l-6.6 3.9 1.8-7.4L1.5 9.6 9 9z"/></svg></h1>
  <div class="steps">
    <div class="step done"><svg width="15" height="15" viewBox="0 0 20 20"><circle cx="10" cy="10" r="10" fill="var(--green)"/><path d="M5.5 10l3 3 6-6" stroke="#fff" stroke-width="2" fill="none"/></svg>Review 1</div>
    <span class="dots"></span>
    <div class="step done"><svg width="15" height="15" viewBox="0 0 20 20"><circle cx="10" cy="10" r="10" fill="var(--green)"/><path d="M5.5 10l3 3 6-6" stroke="#fff" stroke-width="2" fill="none"/></svg>Review 2</div>
    <span class="dots"></span>
    <div class="step now"><svg width="15" height="15" viewBox="0 0 20 20"><circle cx="10" cy="10" r="10" fill="#fde6e7"/><circle cx="10" cy="10" r="4" fill="var(--accent)"/></svg>Review 3</div>
    <span class="dots"></span>
    <div class="step todo"><svg width="15" height="15" viewBox="0 0 20 20"><circle cx="10" cy="10" r="9" fill="none" stroke="#c4c7cb" stroke-width="1.4"/></svg>Review 4</div>
  </div>
  <div class="start"><svg width="9" height="10" viewBox="0 0 10 12"><path d="M1 1l8 5-8 5z" fill="none" stroke="#fff" stroke-width="1.4"/></svg>Start Review</div>
</section>

<main class="main">
  <div class="section-title" style="top:30px"><svg width="19" height="18" viewBox="0 0 24 22" fill="none" stroke="#1f2328" stroke-width="1.6"><path d="M3 1h12v20H3z"/><circle cx="15" cy="13" r="4"/><path d="M18 16l4 4M6 5h6"/></svg>Description</div>
  <p class="para" style="top:62px">Grab is most commonly used as a <b>verb</b>, meaning <b>to take something quickly or suddenly</b>.</p>

  <div class="section-title" style="top:106px"><svg width="19" height="18" viewBox="0 0 24 22" fill="none" stroke="#1f2328" stroke-width="1.6"><path d="M2 16l10 3 10-3M2 20l10 3 10-3M12 2v7M6 6l2 2M18 6l-2 2M8 13a4 4 0 018 0"/></svg>Example</div>
  <p class="para" style="top:137px">Imagine you're running late for school. You don't have time for breakfast, so you quickly <b>grab</b> an apple from the kitchen and rush out the door. As you reach the bus stop, your friend waves and say, "Hey! Let's <b>grab</b> a coffee after class." Later, wen you sit down, your phone starts ringing. You <b>grab</b> it from your bag and answer.</p>

  <div class="section-title" style="top:211px"><svg width="19" height="18" viewBox="0 0 24 22" fill="none" stroke="#1f2328" stroke-width="1.6"><path d="M1 2h22M3 2v13h18V2M12 15v6M8 21h8M7 11V8M11 11V5M15 11V7"/></svg>Learning Curve Graph</div>

  <div class="chart">
    <svg width="578" height="222" viewBox="0 0 770 296" font-family="Roboto, Arial, sans-serif">
      <rect x="16" y="16" width="738" height="53" fill="#e9eff7"/>
      <rect x="16" y="69" width="738" height="105" fill="#eaf4ec"/>
      <rect x="16" y="174" width="738" height="27" fill="#fdfbea"/>
      <rect x="16" y="201" width="738" height="26" fill="#f0f0f1"/>
      <g font-size="10" fill="#5a5f66">
        <text x="29" y="42">Long-Term Memory</text>
        <text x="29" y="120">Working Memory</text>
        <text x="29" y="187">Short-Term Memory</text>
        <text x="29" y="213">Forgotten Memory</text>
      </g>
      <rect x="125" y="182" width="22" height="45" fill="var(--bar)"/>
      <rect x="245" y="69" width="22" height="158" fill="var(--bar)"/>
      <path d="M156 176 C190 180 220 195 243 218" stroke="#444" stroke-width="1.5" stroke-dasharray="1.5 4" fill="none"/>
      <path d="M270 70 C330 78 360 80 390 95 C430 115 470 170 495 225" stroke="#444" stroke-width="1.5" stroke-dasharray="1.5 4" fill="none"/>
      <g font-size="9" fill="#1f2328" text-anchor="middle">
        <rect x="92" y="159" width="58" height="21" rx="3" fill="#fff" stroke="#d4d6da"/>
        <text x="121" y="173">May 18</text>
        <rect x="198" y="53" width="58" height="21" rx="3" fill="#fff" stroke="#d4d6da"/>
        <text x="227" y="67">May 19</text>
      </g>
      <path d="M16 227H754" stroke="#333" stroke-width="1.2"/>
      <g stroke="#333" stroke-width="1">
        <path d="M30 227v7M90 227v7M150 227v7M210 227v7M270 227v7M330 227v7M390 227v7M450 227v7M510 227v7M570 227v7M630 227v7M690 227v7M750 227v7"/>
      </g>
      <g font-size="10" fill="#1f2328" text-anchor="middle">
        <text x="34" y="251">18 May</text><text x="90" y="251">12:00</text>
        <text x="150" y="251">19 May</text><text x="210" y="251">12:00</text>
        <text x="270" y="251">20 May</text><text x="330" y="251">12:00</text>
        <text x="390" y="251">21 May</text><text x="450" y="251">12:00</text>
        <text x="510" y="251">22 May</text><text x="570" y="251">12:00</text>
        <text x="630" y="251">23 May</text><text x="690" y="251">12:00</text>
        <text x="744" y="251">24 M</text>
        <text x="385" y="275" font-size="11">Date Range</text>
      </g>
    </svg>
  </div>
</main>

<aside class="analysis">
  <h2><svg width="19" height="18" viewBox="0 0 24 22" fill="none" stroke="#1f2328" stroke-width="1.6"><circle cx="12" cy="5" r="3"/><circle cx="4" cy="9" r="2.5"/><circle cx="20" cy="9" r="2.5"/><path d="M6 21a6 6 0 0112 0M1 18a4 4 0 015-3M23 18a4 4 0 00-5-3"/></svg>QuillaVorn Tutor Learning Analysis</h2>
  <p>Lorem ipsum dolor sit amet, consectetur adipiscing elit, sed do eiusmod tempor incididunt ut labore et dolore magna aliqua.</p>
  <p>Ut enim ad minim veniam, quis nostrud exercitation ullamco laboris nisi ut aliquip ex ea commodo consequat.</p>
  <p>Excepteur sint occaecat cupidatat non proident, sunt in culpa qui officia deserunt mollit anim id est laborum.</p>
  <p>Duis aute irure dolor in reprehenderit in voluptate velit esse cillum dolore eu fugiat nulla pariatur.</p>
</aside>
</body>
</html>
```